Non-Profit Needs Plastic Recycling Infographic

We need a modern infographic to help illustrate international recycling rates for expanded polystyrene plastic. Include the information below and use the attached PowerPoint as an example for your design – the PowerPoint is just to illustrate the information; you do not need to follow it completely.

We have also included our updated color guide.

Please fit the following information into the infographic:
• The one item that is necessary is the global map – the "Global EPS Packaging Recycling" header is not required
• Do NOT include any "chasing arrows" recycling symbols
• the "34 Countries" should read "34 Countries with a Confirmed Recycling Rate"
• "34 Countries" should be an information block along with the "21 Countries"
• The "32 Countries" and "62 Countries" should be included in the graph image – we have given a pie graph as an example, though it can be another graph
• "Leading EPS Recyclate Sources" should have the following four blocks associated with it: Automotive, Seafood & Fishers, Furniture, and Appliances; use attached photos for blocks
• The lorem ipsum vertical information blocks should include 3 columns:
#1: "Developing Countries Recycle EPS" – include country outline of Guatemala; include the text "EPS manufacturing is working with government in Guatemala. Where an EPS molder exists is the easiest way to initiate EPS recycling. Work with the EPS manufacturing sector can promote quick startup of B2B recycling programs."
#2: "Small Islands Recycle EPS" – include country outline of Dominican Republic; include the text "An EPS recycling program in the Dominican Republic highlighted the need for new polystyrene recycling technologies. Through their work with machinery specialists, they were able to identify a solution that then spread to other nations."
#3: "Local Communities Recycle EPS" – include country outline of China; include text "EPS startups can lead to successful recycling collection programs. Tulvenka Neighborhood Office in Xiamen City, China, was already receiving polystyrene for recycling when they were able to procure a densifier. Since installation, the program has spread to five machines located across the city."
• Under the "Varnholt Waste Stewardship Accord" statement, include the following: "Criteria could be tailored to specific applications, allowing for country-specific flexibility. This approach would also help to develop standards on a material basis and allow countries to focus on scientific research and assess availability of recycling programs."

Sans Serif

• 1. Global EPS Recycling Map (see attached documents), 2. Infographic should be vertical in design, NOT horizontal
• Chasing Arrows Recycling Symbols

```html
<!DOCTYPE html>
<html lang="en">
<head>
<meta charset="UTF-8">
<title>EPS Recycling Infographic</title>
<link href="https://fonts.googleapis.com/css2?family=Carlito:wght@400;700&display=swap" rel="stylesheet">
<style>
:root{
  --stage:#000000;
  --navy:#263a78;
  --ink:#141a40;
  --card:#161a45;
  --cream:#fdf5ec;
  --sage:#eeefe6;
  --white:#ffffff;
  --orange:#f97f38;
  --gold:#f5b800;
  --teal:#173c3a;
  --blue-text:#2a3a7a;
  --grey-text:#555555;
  --pie-blue:#5b9bd5;
  --pie-orange:#ed7d31;
  --pie-grey:#a5a5a5;
  --map-land:#d9d4cf;
}
*{box-sizing:border-box;margin:0;padding:0}
html,body{width:1200px;height:675px;overflow:hidden;background:var(--stage)}
body{font-family:"Carlito",sans-serif;position:relative}
.infographic{position:absolute;left:421px;top:0;width:359px;height:675px;overflow:hidden}
.band{position:absolute;left:0;width:359px}
.band--hero{top:0;height:177px;background:var(--navy)}
.band--sectors{top:177px;height:81px;background:var(--sage)}
.band--stats{top:258px;height:98px;background:var(--white)}
.band--cases{top:356px;height:216px;background:var(--orange)}
.band--accord{top:572px;height:103px;background:var(--ink)}

.map-disc{position:absolute;left:108px;top:15px;width:142px;height:142px;border-radius:50%;background:var(--cream)}
.map-ribbon{position:absolute;left:20px;top:34px;width:102px;height:9px;background:#4a4a4a;color:var(--white);font-size:4.6px;font-weight:700;text-align:center;line-height:9px}
.map-area{position:absolute;left:18px;top:46px;width:106px;height:62px;border-radius:6px;background:linear-gradient(90deg,#a9b43a 0%,var(--map-land) 45%,#a9b43a 70%,#1d2a4a 100%)}
.map-key{position:absolute;left:18px;top:104px;width:110px;display:flex;gap:5px;font-size:2.6px;color:#777;align-items:center}
.map-key span{display:flex;align-items:center;gap:1.5px}
.map-key i{display:inline-block;width:2.5px;height:2.5px}

.pie-title{position:absolute;left:50px;top:185px;font-size:5px;color:var(--grey-text);width:62px;text-align:center}
.pie{position:absolute;left:59px;top:197px;width:37px;height:37px}
.pie-legend{position:absolute;left:39px;top:243px;display:flex;gap:6px;font-size:5.4px;color:var(--grey-text)}
.pie-legend span{display:flex;align-items:center;gap:2px}
.pie-legend i{display:inline-block;width:3px;height:3px}

.sector{position:absolute;display:flex;align-items:center;gap:6px;font-size:9.6px;color:#222}
.sector-photo{width:22px;height:22px;border-radius:50%;background:radial-gradient(circle,#f2f2f2 40%,#c9c9c9 100%);box-shadow:0 1px 2px rgba(0,0,0,.25);flex:none}
.sector--furniture{left:148px;top:192px}
.sector--fisheries{left:240px;top:191px}
.sector--automotive{left:148px;top:223px}
.sector--appliances{left:243px;top:222px}

.stat{position:absolute;top:280px;display:flex;align-items:center;gap:4px}
.stat-number{font-size:42px;line-height:1;letter-spacing:-1px}
.stat-label{font-size:9.6px;font-weight:700;line-height:12.9px}
.stat--confirmed{left:37px}
.stat--confirmed .stat-number{color:var(--gold)}
.stat--confirmed .stat-label{color:var(--grey-text)}
.stat--above{left:182px}
.stat--above .stat-number{color:var(--teal)}
.stat--above .stat-label{color:var(--blue-text)}

.case{position:absolute;top:387px;width:97px;height:123px;background:var(--card);padding:0 9px}
.case--guatemala{left:19px}
.case--dominican{left:135px}
.case--china{left:247px;top:387px}
.case-outline{display:block;margin:12px auto 0;width:24px;height:23px;border-radius:40% 55% 45% 50%}
.case--guatemala .case-outline{background:#e6e6e6;width:20px}
.case--dominican .case-outline{background:#f39a1e;width:38px;height:20px;border-radius:45% 60% 40% 50%}
.case--china .case-outline{background:#d0201f;width:32px}
.case-title{margin-top:5px;font-size:4.5px;color:var(--gold);line-height:6px}
.case-body{margin-top:4px;font-size:4.2px;color:var(--white);line-height:6.3px}

.accord-title{position:absolute;left:49px;top:591px;font-size:10.6px;color:var(--gold)}
.accord-body{position:absolute;left:50px;top:609px;width:266px;font-size:8.4px;line-height:11.6px;color:var(--white)}
</style>
</head>
<body>
<main class="infographic">
  <section class="band band--hero">
    <div class="map-disc">
      <div class="map-ribbon">Global EPS Packaging Recycling</div>
      <div class="map-area" role="img" aria-label="World map shading countries by EPS packaging recycling rate"></div>
      <div class="map-key">
        <span>Key</span>
        <span><i style="background:#a9b43a"></i>Rate above 30%</span>
        <span><i style="background:#1d2a4a"></i>Rate below 30%</span>
        <span><i style="background:#d9d4cf"></i>No data</span>
      </div>
    </div>
  </section>

  <section class="band band--sectors"></section>
  <div class="pie-title">EPS Using Countries</div>
  <svg class="pie" viewBox="0 0 36 36" aria-label="Pie chart of EPS using countries">
    <path d="M18 18 L18 0 A18 18 0 0 1 35.73 21.13 Z" fill="var(--pie-blue)"/>
    <path d="M18 18 L35.73 21.13 A18 18 0 0 1 19.57 35.93 Z" fill="var(--pie-orange)"/>
    <path d="M18 18 L19.57 35.93 A18 18 0 0 1 18 0 Z" fill="var(--pie-grey)"/>
  </svg>
  <div class="pie-legend">
    <span><i style="background:var(--pie-blue)"></i>EPS 1</span>
    <span><i style="background:var(--pie-orange)"></i>EPS 2</span>
    <span><i style="background:var(--pie-grey)"></i>No EPS</span>
  </div>
  <div class="sector sector--furniture"><span class="sector-photo" role="img" aria-label="Furniture photo"></span>Furnitures</div>
  <div class="sector sector--fisheries"><span class="sector-photo" role="img" aria-label="Fisheries photo"></span>Fisheries</div>
  <div class="sector sector--automotive"><span class="sector-photo" role="img" aria-label="Automotive part photo"></span>Automotive</div>
  <div class="sector sector--appliances"><span class="sector-photo" role="img" aria-label="Appliances photo"></span>Appliances</div>

  <section class="band band--stats"></section>
  <div class="stat stat--confirmed">
    <span class="stat-number">34</span>
    <span class="stat-label">Countries<br>with a Confirmed<br>Recycling Rate</span>
  </div>
  <div class="stat stat--above">
    <span class="stat-number">21</span>
    <span class="stat-label">Countries<br>Have a Recycling<br>Rate above 30%</span>
  </div>

  <section class="band band--cases"></section>
  <article class="case case--guatemala">
    <span class="case-outline" role="img" aria-label="Country outline of Guatemala"></span>
    <h3 class="case-title">Developing Countries Recycle EPS</h3>
    <p class="case-body">EPS manufacturing is working with government in Guatemala. Where an EPS molder exists is the easiest way to initiate EPS recycling. Work with the EPS manufacturing sector can promote quick startup of B2B recycling programs.</p>
  </article>
  <article class="case case--dominican">
    <span class="case-outline" role="img" aria-label="Country outline of the Dominican Republic"></span>
    <h3 class="case-title">Small Islands Recycle EPS</h3>
    <p class="case-body">An EPS recycling program in the Dominican Republic highlighted the need for new polystyrene recycling technologies. Through their work with machinery specialists, they were able to identify a solution that then spread to other nations.</p>
  </article>
  <article class="case case--china">
    <span class="case-outline" role="img" aria-label="Country outline of China"></span>
    <h3 class="case-title">Local Communities Recycle EPS</h3>
    <p class="case-body">EPS startups can lead to successful recycling collection programs. Tulvenka Neighborhood Office in Xiamen City, China, was already receiving polystyrene for recycling when they were able to procure a densifier. Since installation, the program has spread to five machines located across the city.</p>
  </article>

  <section class="band band--accord"></section>
  <h2 class="accord-title">Varnholt Waste Stewardship Accord</h2>
  <p class="accord-body">Criteria could be tailored to specific applications, allowing for country-specific flexibility. This approach would also help to develop standards on a material basis and allow countries to focus on scientific research and assess availability of recycling programs.</p>
</main>
</body>
</html>
```